Hollarin Painting

Need business card design

Target Market(s)

Paint

Industry/Entity Type

Painting

Requirements
Must have
• Brice Halvorsen | Superviser
| HollaRin Painting
| mobile: (360) 555-0148
| email: Brice@hollarininc.example
| site: www.hollarininc.example
| address: 718 Marbeck St NE Ste 300, Olympia, WA 98577

```html
<!DOCTYPE html>
<html lang="en">
<head>
<meta charset="utf-8">
<title>Hollarin Painting — Business Card</title>
<link rel="stylesheet" href="https://fonts.googleapis.com/css2?family=Tinos:wght@400;700&family=Roboto:wght@400;500&display=swap">
<style>
  :root {
    --navy: #233f85;
    --green: #62b946;
    --green-dark: #3f8a2c;
    --white: #ffffff;
    --backdrop: #d4d4d4;
  }
  * { margin: 0; padding: 0; box-sizing: border-box; }
  html, body {
    width: 1200px; height: 852px; overflow: hidden;
    background: var(--backdrop);
  }
  .canvas {
    position: relative; width: 1200px; height: 852px;
  }
  .card {
    position: absolute; top: 266px;
    width: 560px; height: 320px;
    border-radius: 18px; overflow: hidden;
    box-shadow: 0 6px 16px rgba(0,0,0,0.22);
  }
  .card--front { left: 30px; background: var(--navy); }
  .card--back { left: 610px; background: var(--white); }

  .brand {
    position: absolute; display: flex; align-items: center; gap: 12px;
    font-family: "Tinos", "Times New Roman", serif; font-weight: 700;
    font-size: 34px; letter-spacing: 0.5px; white-space: nowrap;
  }
  .brand__dot { width: 22px; height: 22px; border-radius: 50%; }
  .card--front .brand { left: 50%; top: 50%; transform: translate(-50%, -50%); color: var(--white); }
  .card--front .brand__dot { background: var(--white); }
  .card--back .brand { left: 24px; top: 226px; color: var(--navy); font-size: 26px; }
  .card--back .brand__dot { background: var(--navy); width: 18px; height: 18px; }

  .back-panel { position: absolute; inset: 0; }

  .name-band {
    position: absolute; left: 190px; top: 62px;
    color: var(--navy);
  }
  .name-band__name {
    font-family: "Tinos", "Times New Roman", serif; font-weight: 700;
    font-size: 24px; letter-spacing: 0.5px; text-transform: uppercase; line-height: 1;
  }
  .name-band__title {
    font-family: "Roboto", Arial, sans-serif; font-size: 14px; color: var(--white);
    margin-top: 4px; padding-left: 18px;
  }

  .contact {
    position: absolute; left: 296px; top: 150px;
    font-family: "Roboto", Arial, sans-serif; font-size: 13px; line-height: 1.4;
    color: var(--white);
  }
  .contact__address { margin-bottom: 10px; }
  .contact__row { display: flex; align-items: center; gap: 8px; margin-bottom: 5px; }
  .contact__icon { width: 18px; height: 18px; flex: none; }
</style>
</head>
<body>
<main class="canvas">

  <section class="card card--front" aria-label="Card front">
    <div class="brand"><span class="brand__dot"></span>Hollarin Painting</div>
  </section>

  <section class="card card--back" aria-label="Card back">
    <svg class="back-panel" width="560" height="320" viewBox="0 0 560 320">
      <polygon points="215,0 560,0 560,320 330,320" fill="var(--navy)"/>
      <polygon points="175,58 560,58 560,108 190,108" fill="var(--green)"/>
      <polygon points="190,108 230,108 230,120" fill="var(--green-dark)"/>
    </svg>

    <div class="brand"><span class="brand__dot"></span>HollaRin Painting</div>

    <div class="name-band">
      <div class="name-band__name">Brice Halvorsen</div>
      <div class="name-band__title">Superviser</div>
    </div>

    <div class="contact">
      <p class="contact__address">718 Marbeck St NE Ste 300,<br>Olympia, WA 98577</p>
      <p class="contact__row">
        <svg class="contact__icon" viewBox="0 0 18 18"><circle cx="9" cy="9" r="9" fill="var(--green)"/><path d="M6 5l2 0 1 2-1.2 1a5 5 0 0 0 2.2 2.2L11 9l2 1v2c-4 .5-7.5-3-7-7z" fill="var(--white)"/></svg>
        (360) 555-0148
      </p>
      <p class="contact__row">
        <svg class="contact__icon" viewBox="0 0 18 18"><circle cx="9" cy="9" r="9" fill="var(--green)"/><rect x="4.5" y="6" width="9" height="6.5" fill="var(--white)"/><path d="M4.5 6l4.5 3.5L13.5 6" fill="none" stroke="var(--green)" stroke-width="1"/></svg>
        Brice@hollarininc.example
      </p>
      <p class="contact__row">
        <svg class="contact__icon" viewBox="0 0 18 18"><circle cx="9" cy="9" r="9" fill="var(--green)"/><circle cx="9" cy="9" r="4.5" fill="none" stroke="var(--white)" stroke-width="1.2"/><path d="M4.5 9h9M9 4.5c-2 2.5-2 6.5 0 9M9 4.5c2 2.5 2 6.5 0 9" fill="none" stroke="var(--white)" stroke-width="1"/></svg>
        www.hollarininc.example
      </p>
    </div>
  </section>

</main>
</body>
</html>
```